Beautiful Customer Appreciation Gift Box Need Eye Catching Brochure

I need a brochure to include with small sample gift boxes that I send or give to companies who do door to door marketing of businesses, company reps, real estate designers and large companies looking for a unique customer appreciation gifts.

The brochure needs to capture the size variations and the limitless options for their budget and customization needs.

They are gift boxes that can be filled with cookies for the drug rep making an impression for the doc - after cookies are gone, the gift remains

At christmas, we fill them with baked goods and provide to each office. Every year as i visit the offices, they have last years gift box out as a decoration.

realtors can use them as a welcome to your new home gift filled with a bottle of wine and their papers left on the kitchen counter

We have had them used for baby shower gifts, kept later as a decoration.

that's the concept, i need it captured.
Marlowe's Seasonal Nook is the current name
a tag line we came up with is Every bit in the WRAPPINGtouch.

Reason: We are very close, I have my photoshoot tomorrow and I'd like to see and continue to tweek the current designs. I have pretty well deleted the designs we are not considering at this point. The others all have components we love. So I need a little more time and some tweaking to decide for sure.

Target Market(s)

the target is the company or individuals looking for gift giving options for clients and customers. From the door to door salesperson looking to make a splash or big impression to the large company looking for nice corporate gift ideas.

The concept of say goodbye to plain jane gift boxes that all look alike... Say goodbye to expensive gift wrap and bows that get thrown away in minutes.... and hello to a beautiful custom made gift box that will remain a decoration or keepsake box forever....

Industry/Entity Type

Retail

Font styles to use
Sans Serif
Script

Requirements
Must have
• IMPORTANT... I CAN and AM GETTING better pictures for the printing purposes. I'm looking more for the concept of the brochuure and layout design.
• I'd love to have it have some place holders for various pictures and descriptions - because each industry targets different people, I'd like to be able to change the front cover of the brochure with a picture of a box that targets that audience a little.
• For a real estate person... i might choose a beautiful centerpiece looking one... vs, the ob/gyn office, I might choose a baby one.
• I have some design skill, just 0 times and the programs have changed alot over the years, so this may go on to future work and a long design relationship as the company grows and changes. I do know photoshop and pagemaker from long ago so I should be able to drop in pics and text options. if we use compatible programs.
Nice to have
• would love to have some kind of background for the page - not just plain white background.
• i like angles and curves
Should not have
• boxy look.

```html
<!DOCTYPE html>
<html lang="en">
<head>
<meta charset="utf-8">
<title>Marlowe's Seasonal Nook – Trifold Outside</title>
<link href="https://fonts.googleapis.com/css2?family=Arimo:wght@400;700&family=Great+Vibes&family=Roboto:wght@400;700&display=swap" rel="stylesheet">
<style>
  :root {
    --page-bg: #e6e6e6;
    --cream: #f6dfb0;
    --lavender: #c897c6;
    --lavender-light: #d9b3d7;
    --plum: #8c3b8a;
    --plum-deep: #741d70;
    --white: #ffffff;
    --text-plum: #7a1f74;
  }
  * { margin: 0; padding: 0; box-sizing: border-box; }
  html, body {
    width: 1200px; height: 800px; overflow: hidden;
    background: var(--page-bg);
  }
  .brochure {
    position: absolute; left: 120px; top: 29px;
    width: 960px; height: 742px;
    background: var(--cream);
    box-shadow: 0 10px 30px rgba(0,0,0,.18);
    overflow: hidden;
  }
  .brochure-art { position: absolute; inset: 0; width: 960px; height: 742px; }
  .panel-text { position: absolute; font-family: "Arimo", Arial, sans-serif; color: var(--text-plum); }
  .section-title { font-weight: 700; font-size: 17px; letter-spacing: .3px; text-transform: uppercase; margin-bottom: 10px; }
  .section-body { font-size: 11.5px; line-height: 1.4; margin-bottom: 10px; }
  .about { left: 40px; top: 395px; width: 255px; }
  .keepsakes { left: 360px; top: 235px; width: 250px; }
  .contact {
    position: absolute; left: 320px; top: 560px; width: 320px;
    text-align: center; color: var(--white);
    font-family: "Roboto", Arial, sans-serif;
  }
  .contact-title { font-weight: 700; font-size: 14px; letter-spacing: .5px; margin-bottom: 10px; }
  .contact-phone { font-weight: 700; font-size: 22px; letter-spacing: .5px; margin-bottom: 6px; }
  .contact-line { font-size: 13px; line-height: 1.45; }
  .brand-name {
    position: absolute; left: 660px; top: 70px; width: 280px;
    text-align: center;
    font-family: "Great Vibes", cursive;
    font-size: 58px; line-height: .95;
    color: var(--plum-deep);
  }
  .tagline-script {
    position: absolute; left: 662px; top: 378px; width: 290px;
    font-family: "Great Vibes", cursive;
    font-size: 30px; color: var(--plum);
    transform: rotate(-4deg);
    transform-origin: left center;
  }
  .gift-boxes-label {
    position: absolute; left: 842px; top: 498px; width: 110px;
    font-family: "Great Vibes", cursive;
    font-size: 32px; line-height: .9; color: var(--white);
  }
</style>
</head>
<body>
<main class="brochure">
  <svg class="brochure-art" viewBox="0 0 960 742" xmlns="http://www.w3.org/2000/svg">
    <defs>
      <linearGradient id="bouquetTone" x1="0" y1="0" x2="1" y2="1">
        <stop offset="0" stop-color="#6d7a5a"/>
        <stop offset=".45" stop-color="#e27ab8"/>
        <stop offset="1" stop-color="#8a7bc4"/>
      </linearGradient>
      <radialGradient id="boxTone" cx=".5" cy=".5" r=".6">
        <stop offset="0" stop-color="#7a5a3a"/>
        <stop offset=".6" stop-color="#3d3a6a"/>
        <stop offset="1" stop-color="#4e6a45"/>
      </radialGradient>
    </defs>

    <!-- top lavender sweep across middle and right panels -->
    <path class="top-band" d="M320 0 H960 V70 C860 50 760 30 640 55 C540 75 430 40 320 60 Z" fill="var(--lavender-light)"/>
    <path class="top-stripe" d="M320 34 C430 18 540 52 640 36 C760 14 860 34 960 46 V58 C860 44 760 26 640 48 C540 66 430 32 320 46 Z" fill="var(--plum)"/>

    <!-- white swoosh -->
    <path class="white-swoosh" d="M0 540 C200 525 420 470 600 440 C760 412 860 382 960 360 V400 C860 422 760 452 600 482 C420 512 200 572 0 590 Z" fill="var(--white)"/>
    <!-- plum stripe -->
    <path class="plum-stripe" d="M0 590 C200 572 420 512 600 482 C760 452 860 422 960 400 V420 C860 442 760 472 600 502 C420 532 200 592 0 612 Z" fill="var(--plum)"/>
    <!-- lavender base -->
    <path class="lavender-base" d="M0 612 C200 592 420 532 600 502 C760 472 860 442 960 420 V742 H0 Z" fill="var(--lavender)"/>

    <!-- fold lines -->
    <line x1="320" y1="0" x2="320" y2="742" stroke="rgba(0,0,0,.06)" stroke-width="1"/>
    <line x1="640" y1="0" x2="640" y2="742" stroke="rgba(0,0,0,.06)" stroke-width="1"/>

    <!-- cover photo placeholder -->
    <g role="img" aria-label="Photo of a floral centerpiece gift box with pink and purple silk flowers">
      <path d="M0 0 H320 V230 C305 240 300 270 280 275 H40 C20 270 15 240 0 235 Z" fill="url(#bouquetTone)" stroke="var(--white)" stroke-width="4"/>
    </g>

    <!-- keepsake box photo -->
    <g role="img" aria-label="Photo of a custom keepsake gift box">
      <circle cx="560" cy="128" r="62" fill="url(#boxTone)" stroke="var(--plum)" stroke-width="5"/>
      <circle cx="560" cy="128" r="67" fill="none" stroke="var(--white)" stroke-width="3"/>
    </g>

    <!-- right panel gift box photos -->
    <g role="img" aria-label="Photo of a small decorated gift box">
      <circle cx="876" cy="430" r="42" fill="url(#boxTone)" stroke="var(--plum)" stroke-width="5"/>
      <circle cx="876" cy="430" r="47" fill="none" stroke="var(--white)" stroke-width="3"/>
    </g>
    <g role="img" aria-label="Photo of a large decorated gift box">
      <circle cx="760" cy="520" r="56" fill="url(#boxTone)" stroke="var(--plum)" stroke-width="5"/>
      <circle cx="760" cy="520" r="61" fill="none" stroke="var(--white)" stroke-width="3"/>
    </g>
  </svg>

  <section class="panel-text about">
    <h2 class="section-title">About Our Products</h2>
    <p class="section-body">Lorem ipsum dolor sit amet, consectetur adipiscing elit, sed do eiusmod tempor incididunt ut labore et dolore magna aliqua.</p>
    <p class="section-body">Ut enim ad minim veniam, quis nostrud exercitation ullamco laboris nisi ut aliquip ex ea commodo consequat.</p>
  </section>

  <section class="panel-text keepsakes">
    <h2 class="section-title">Custom Keepsakes</h2>
    <p class="section-body">Say goodbye to plain jane gift boxes that all look alike... Say goodbye to expensive gift wrap and bows that get thrown away in minutes... And hello to a beautiful custom made gift box that will remain a decoration or keepsake box forever...</p>
  </section>

  <section class="contact">
    <h2 class="contact-title">CONTACT US</h2>
    <p class="contact-phone">555-204-7781</p>
    <p class="contact-line">e-mail: hello@seasonalnook.net</p>
    <p class="contact-line">web: marlowesnook.com</p>
  </section>

  <h1 class="brand-name">Marlowe's Seasonal Nook</h1>
  <p class="tagline-script">Beautiful, Custom Made</p>
  <p class="gift-boxes-label">Gift<br>&nbsp;&nbsp;Boxes</p>
</main>
</body>
</html>
```